BRONT (Bright Routing Online Network Tools) Letter Head Design Project

Company Name: BRONT (Bright Routing Online Network Tools) JLT.
Office Address: Office No 718, Saffron Crest Building, Marwah Garden Quarter, Dubai, U.A.E
Company line of business:
1) Currently we have a POS solution for retail outlets like duty free shops, supermarkets, department stores etc... The solution is deployed in Palmgate Travel Retail on 350 POS and in Corniche Transit Stores on 100 POS. So our main line of business is the deployment of this solution in retail outlets locally or regionally. We have already deployed the solution in India and Australia.
2) Integration of other third party POS systems with an online credit authorization netwotk in the UAE. This will enable POS applications to connect directly to the acquiring banks without needing an EFT terminal like Paxolan or Trenvira. The credit card payment is completed at the POS.
3) Other solutions that are targeting retail outlets like mobile POS, queue busting solutions, stock taking solutions using hand held devices, transaction capture systems, etc...
4) Other IT services like support of call center solutions from Orbisan Callworks and development of new solutions as per customer requirements.
We need a letter head design for the company. We don't have any specific requirements in mind and we prefer to leave it up to the designers to come up with creative designs that will not be limited by any guidelines.
Updates
I have just uploaded all the files I received from my company logo designer. Please review and let me know if you need anything else. .
Dear All,
I have received very nice designs and I thank you for all the hard work you have put so far. I would like the letter head to have all the following company details:
Office Address: Office No 718, Saffron Crest Building, MGQ, Dubai UAE
P.O.Box: 58316 Dubai UAE
Tel Number:+971-4-5817260
Fax Number::+971-4-5817261
Website:www.brontmgq.example
I would also like to represent the company details as a QRCode somewhere on the page, probably next to the company details if possible (as a trial).
In case you have included a butterfly in the middle of the page as part of your design, I prefer that it doesn't include any colors as colors might make reading the text on the page more difficult.
I don't want to have too many butterflies on the page. 2 are more than enough.
Can you also include a design for the continuation pages?
Thank you in advance and I look forward to receiving your creative designs.
Regards
Samir Toufany

```html
<!DOCTYPE html>
<html lang="en">
<head>
<meta charset="utf-8">
<title>BRONT Letterhead</title>
<link rel="stylesheet" href="https://fonts.googleapis.com/css2?family=Jost:wght@400;500&display=swap">
<style>
  :root {
    --panel-dark: #414141;
    --panel-light: #6e6e6e;
    --paper: #ffffff;
    --accent-lime: #c8d400;
    --accent-blue: #0a8ee0;
    --ink-light: #f2f2f2;
    --ink-soft: #d9d9d9;
    --code-fill: #e9e9e9;
    --backdrop: #e6e6e6;
  }
  html, body {
    margin: 0;
    padding: 0;
    overflow: hidden;
    background: var(--backdrop);
  }
  .letterhead {
    position: relative;
    width: 1019px;
    height: 1200px;
    overflow: hidden;
    background: var(--paper);
    font-family: "Jost", "Futura", sans-serif;
  }
  .letterhead__art {
    position: absolute;
    inset: 0;
    width: 1019px;
    height: 1200px;
    display: block;
  }
  .brand {
    position: absolute;
    left: 44px;
    top: 70px;
    display: flex;
    align-items: center;
    gap: 16px;
  }
  .brand__dot {
    width: 30px;
    height: 30px;
    border-radius: 50%;
    background: var(--accent-blue);
  }
  .brand__name {
    font-size: 66px;
    font-weight: 400;
    letter-spacing: 3px;
    line-height: 1;
    color: var(--ink-light);
  }
  .office-address {
    position: absolute;
    left: 44px;
    top: 176px;
    margin: 0;
    font-style: normal;
    font-size: 15px;
    line-height: 1.4;
    color: var(--ink-soft);
  }
  .contact-list {
    position: absolute;
    left: 44px;
    top: 262px;
    margin: 0;
    padding: 0;
    list-style: none;
    font-size: 14px;
    line-height: 1.45;
    color: var(--ink-soft);
  }
  .contact-qr {
    position: absolute;
    left: 44px;
    top: 372px;
    width: 80px;
    height: 80px;
    background: var(--code-fill);
  }
</style>
</head>
<body>
  <main class="letterhead">
    <svg class="letterhead__art" viewBox="0 0 1019 1200" xmlns="http://www.w3.org/2000/svg" aria-hidden="true">
      <defs>
        <linearGradient id="panelShade" x1="0" y1="0" x2="1" y2="0">
          <stop offset="0" stop-color="var(--panel-dark)"/>
          <stop offset="0.35" stop-color="var(--panel-light)"/>
          <stop offset="1" stop-color="var(--panel-dark)"/>
        </linearGradient>
        <clipPath id="limeBand"><rect x="0" y="380" width="1019" height="640"/></clipPath>
        <clipPath id="blueBand"><rect x="0" y="1030" width="1019" height="170"/></clipPath>
      </defs>
      <rect class="side-panel" x="0" y="0" width="1019" height="1200" fill="url(#panelShade)"/>
      <path class="edge-lime" clip-path="url(#limeBand)" transform="translate(-11 0)" fill="var(--accent-lime)"
            d="M540,0 H1019 V1200 H420 C280,1080 150,900 150,650 C150,420 260,230 450,130 C505,100 535,60 540,0 Z"/>
      <path class="edge-blue" clip-path="url(#blueBand)" transform="translate(-4 6)" fill="var(--accent-blue)"
            d="M540,0 H1019 V1200 H420 C280,1080 150,900 150,650 C150,420 260,230 450,130 C505,100 535,60 540,0 Z"/>
      <path class="writing-area" fill="var(--paper)"
            d="M540,0 H1019 V1200 H420 C280,1080 150,900 150,650 C150,420 260,230 450,130 C505,100 535,60 540,0 Z"/>
    </svg>

    <div class="brand">
      <span class="brand__dot"></span>
      <span class="brand__name">BRONT</span>
    </div>

    <address class="office-address">
      Office No 718, Saffron Crest Building,<br>
      Marwah Garden Quarter,<br>
      Dubai, U.A.E
    </address>

    <ul class="contact-list">
      <li>P.O.Box: 58316 Dubai UAE</li>
      <li>Tel: +971-4-5817260</li>
      <li>Fax: +971-4-5817261</li>
      <li>www.brontmgq.example</li>
    </ul>

    <div class="contact-qr" role="img" aria-label="QR code holding the company contact details"></div>
  </main>
</body>
</html>
```